Design some Business Cards for Birch Meadow

could someone please design some snazzy business cards for "Birch Meadow"
the website is birchmeadow.co.nz

the logo is attached

name : Harriet Doucan
Contact Number: 0224819357
email: harrietdouc@birchmeadow.co.nz
Slogan: Competitive prices, and personal service in the Wanganui district

The theme is green as its for a lawn mowing outfit!

```html
<!DOCTYPE html>
<html lang="en">
<head>
<meta charset="utf-8">
<title>Birch Meadow – Business Card</title>
<link rel="stylesheet" href="https://fonts.googleapis.com/css2?family=Carlito:wght@400;700&display=swap">
<style>
  :root {
    --backdrop: #000000;
    --card-light: #ffffff;
    --card-dark: #333333;
    --leaf: #95be5e;
    --olive: #5f7314;
    --ink-dark: #262626;
    --contact-green: #9cc766;
  }
  * { margin: 0; padding: 0; box-sizing: border-box; }
  html, body {
    width: 1200px; height: 938px; overflow: hidden;
    background: var(--backdrop);
    font-family: "Carlito", "Calibri", sans-serif;
  }
  .canvas { position: relative; width: 1200px; height: 938px; }

  .card { position: absolute; top: 63px; width: 518px; height: 819px; overflow: hidden; }
  .card--front { left: 69px; background: var(--card-light); }
  .card--back { left: 619px; background: var(--card-dark); }

  .band { position: absolute; left: 0; width: 100%; background: var(--leaf);
    display: flex; align-items: center; justify-content: center; }

  .front__web { top: 127px; height: 66px; color: #fff; font-size: 26px; }

  .brand { position: absolute; left: 0; width: 100%;
    display: flex; align-items: center; justify-content: center; gap: 12px;
    color: var(--olive); font-weight: 700; }
  .brand__dot { width: 18px; height: 18px; border-radius: 50%; background: var(--olive); }
  .front__brand { top: 680px; font-size: 36px; }
  .back__brand { top: 120px; font-size: 32px; }

  .back__name { top: 246px; height: 78px; color: var(--ink-dark); font-size: 38px; }

  .contact { position: absolute; left: 91px; top: 448px; list-style: none;
    color: var(--contact-green); font-size: 21px; line-height: 36px; }
  .contact__label { display: inline-block; width: 40px; }

  .slogan { position: absolute; left: 0; width: 100%; top: 697px;
    text-align: center; color: var(--contact-green); font-size: 25px; line-height: 31px; }

  .back__foot { bottom: 0; height: 28px; }
</style>
</head>
<body>
<main class="canvas">
  <section class="card card--front">
    <div class="band front__web">www.birchmeadow.co.nz</div>
    <div class="brand front__brand"><span class="brand__dot"></span>Birch Meadow</div>
  </section>

  <section class="card card--back">
    <div class="brand back__brand"><span class="brand__dot"></span>Birch Meadow</div>
    <div class="band back__name">Harriet Doucan</div>
    <ul class="contact">
      <li><span class="contact__label">T :</span>0224819357</li>
      <li><span class="contact__label">E :</span>harrietdouc@birchmeadow.co.nz</li>
      <li><span class="contact__label">W :</span>www.birchmeadow.co.nz</li>
    </ul>
    <p class="slogan">Competitive prices, and personal service<br>in the Wanganui district</p>
    <div class="band back__foot"></div>
  </section>
</main>
</body>
</html>
```